Wordpress design for my private practice website - Psychotherapist

I would like a simple, clean, and elegant design for my private practice website. I work with both adults and children so I'd like it to appeal to both. However, since parents make the choice as to where to send their child for therapy, I want it to appeal to adults more. I would like the pictures on the site to have a calming effect - maybe using sand and water and rocks. I am attaching files with my company logo. I would also like my name incorporated into the header - Colette Brannigan, LCSW, Registered Play Therapist. I've also uploaded a picture of myself for my About Page.

I like the design of these 2 website and want something similar:
www.drlorapenwick.example
www.harwood-tallis.example

I would like a home page that highlights a calming graphic across the entire top of the page as well as my practice logo and my name.

I'd like a link to social media sites on the top of the homepage - facebook, pinterest.

I want a simple bar across the top with the following tabs:
Home
About Me (subtabs Who I Am, Specialties and Approach)
Counseling Services (subtabs Individual Counseling, Play Therapy, Sandplay Therapy,)
Fees
FAQs
Contact Me (would love this to be a fill in the blank contact form that sends info to my email address - should include name, phone number, email and a comment box for more information requested)
Blog (this will link with another wordpress blog)

Target Market(s)

Parents of children under age 12 with behavioral problems or are dealing with the breakup of their family through divorce - looking for someone to work with their young child. I also work with Adults that are overwhelmed and worried - often women that have many life stressors and are feeling burnt out on life and meeting everyone's needs. Families going through some type of trauma, including divorce or grief work. I also work with individuals going through a transition of religious beliefs - often exiting the religion of their youth and undergoing a crisis of faith at midlife.

Industry/Entity Type

Mental Health

Contact Information for Business Card

Colette Brannigan, LCSW
Registered Play Therapist
4917 Wexmoor Lane
Idaho Falls, Idaho 83404
(208)555-0187
www.stillbrookcounseling.example

On the opposite side, I'd like an appointment reminder area - with the following text:

Your next appointment is
_____/______/______ at ______am/pm
Please give 24 hrs notice if you need to cancel your appointment.

Coding

Coded - Design and coding required

Number of Pages Required

5+ page

Font styles to use
Sans Serif

Colors
33a6d7
9bcb3c
0355a3

Requirements
Must have
• I'd like it to be a wordpress site. I'm such a newby at web design - but I need to be able to add content and manage the site myself once it is up and running.
Nice to have
• I like the design of these 2 websites and want something similar:
• www.drlorapenwick.example
• www.harwood-tallis.example
• They are clean, easy to navigate and calming.
Should not have
• Should not look like a childcare website.

```html
<!DOCTYPE html>
<html lang="en">
<head>
<meta charset="utf-8">
<title>Stillbrook Counseling – Colette Brannigan</title>
<link rel="stylesheet" href="https://fonts.googleapis.com/css2?family=Raleway:wght@300;400;500&family=Arimo:wght@400;700&display=swap">
<style>
:root{
  --sky:#33a6d7;
  --leaf:#9bcb3c;
  --navy:#0355a3;
  --ink:#222;
  --text:#555;
  --muted:#999;
  --band:#efefef;
  --band-dark:#e6e6e6;
  --field:#eeeeee;
  --btn-grey:#7a7a7a;
  --white:#fff;
}
*{margin:0;padding:0;box-sizing:border-box}
html,body{width:1200px;height:2799px;overflow:hidden}
body{position:relative;background:var(--white);font-family:"Arimo",Arial,sans-serif;color:var(--text)}
.abs{position:absolute}
h1,h2,h3{font-weight:400}

/* hero */
.hero{left:0;top:0;width:1200px;height:657px;
  background:linear-gradient(180deg,#dff1fb 0%,#cfe8f6 12%,#8fb0cc 22%,#46698d 40%,#2c4a6e 60%,#1d3556 100%)}
.hero-stones{left:0;top:134px;width:1200px;height:523px;
  background:radial-gradient(ellipse 520px 160px at 560px 330px,rgba(226,216,190,.55),rgba(226,216,190,0) 70%),
             radial-gradient(ellipse 260px 90px at 900px 200px,rgba(226,216,190,.45),rgba(226,216,190,0) 70%)}
.brand{left:75px;top:22px;width:200px;display:flex;flex-direction:column;align-items:center;gap:10px}
.brand-dot{width:44px;height:44px;border-radius:50%;background:var(--navy)}
.brand-name{font-family:"Raleway",Arial,sans-serif;font-size:17px;letter-spacing:3px;color:#555;text-transform:uppercase}
.main-nav{font-family:"Raleway",Arial,sans-serif;font-size:17px;color:#222}
.main-nav a{color:inherit;text-decoration:none;position:absolute;white-space:nowrap}
.social{top:9px;width:42px;height:42px;border-radius:50%}
.social.fb{left:1024px;background:var(--navy)}
.social.pin{left:1080px;border:1.5px solid #9aa;background:transparent}
.hero-name{left:0;width:1200px;top:440px;text-align:center;font-family:"Raleway",Arial,sans-serif;font-weight:300;font-size:62px;color:var(--white)}
.hero-role{left:0;width:1200px;top:528px;text-align:center;font-family:"Raleway",Arial,sans-serif;font-weight:300;font-size:38px;color:var(--white)}

/* sections */
.section-title{left:0;width:1200px;text-align:center;font-family:"Raleway",Arial,sans-serif;font-weight:400;font-size:42px;color:var(--ink)}
.about-photo{left:205px;top:791px;width:250px;height:250px;border-radius:50%;background:radial-gradient(circle at 50% 45%,#e8cf93 0%,#c9a86a 45%,#8d8360 100%)}
.about-copy{left:535px;top:788px;width:495px;font-size:14.6px;line-height:23.6px;color:#444}
.btn-grey{left:535px;top:1000px;width:166px;height:51px;background:var(--btn-grey);color:var(--white);font-size:17px;display:flex;align-items:center;justify-content:center;border:1px solid #666}

.services{left:0;top:1114px;width:1200px;height:644px;background:var(--band)}
.svc-icon{width:126px;height:126px;border-radius:50%;border:2px solid #555;display:flex;align-items:center;justify-content:center}
.svc-icon.active{background:#666;border-color:#666}
.svc-title{width:340px;text-align:center;font-family:"Raleway",Arial,sans-serif;font-weight:400;font-size:21px;color:#222}
.svc-text{width:340px;text-align:center;font-size:13.6px;line-height:22px;color:#444}
.svc-more{width:340px;text-align:center;font-size:16.5px;color:#444}
.svc-note{left:250px;width:700px;top:1564px;text-align:center;font-size:16px;line-height:30px;color:#aaa}
.btn-outline{left:467px;top:1646px;width:264px;height:52px;border:2px solid var(--navy);color:var(--navy);font-family:"Raleway",Arial,sans-serif;font-size:20px;display:flex;align-items:center;justify-content:center;background:var(--white)}

.blog{left:0;top:1758px;width:1200px;height:313px;background:var(--band-dark)}
.blog-title{left:0;width:1200px;top:1806px;text-align:center;font-family:"Raleway",Arial,sans-serif;font-weight:400;font-size:30px;color:var(--sky)}
.blog-intro{left:320px;width:560px;top:1862px;text-align:center;font-size:13.4px;line-height:22px;color:#222}
.post-title{width:330px;font-family:"Raleway",Arial,sans-serif;font-weight:500;font-size:16.5px;color:#111;white-space:nowrap}
.post-date{font-size:13px;color:var(--muted);display:flex;align-items:center;gap:8px}
.post-text{width:290px;font-size:13.4px;line-height:22px;color:#555}

.field{background:var(--field);font-size:12.5px;color:#999;padding:16px 22px}
.field.focus{background:var(--white);border:1.5px solid #ccc}
.submit{left:116px;top:2370px;width:966px;height:50px;background:var(--sky);color:var(--white);font-family:"Raleway",Arial,sans-serif;font-size:24px;display:flex;align-items:center;justify-content:center}

.footer{left:0;top:2482px;width:1200px;height:317px;background:var(--band)}
.foot-head{font-family:"Raleway",Arial,sans-serif;font-size:23.5px;color:var(--sky);display:flex;align-items:center;gap:16px}
.foot-line{font-size:16px;color:#444}
.foot-link{color:var(--sky)}
.foot-brand{left:78px;top:2572px;width:150px;display:flex;flex-direction:column;align-items:center;gap:8px}
.foot-brand .brand-dot{width:34px;height:34px}
.foot-brand .brand-name{font-size:14px;letter-spacing:2px}
.rule{left:78px;top:2750px;width:1042px;height:1px;background:#888}
.copyright{left:78px;top:2766px;font-size:13.5px;color:#444}
.mini-social{top:2768px;width:16px;height:16px;border-radius:50%;border:1.5px solid var(--sky)}
</style>
</head>
<body>

<div class="abs hero" role="img" aria-label="Calm sea with a row of smooth stepping stones leading to the horizon"></div>
<div class="abs hero-stones"></div>

<header>
  <div class="abs brand"><span class="brand-dot"></span><span class="brand-name">Stillbrook</span></div>
  <nav class="abs main-nav" style="left:0;top:70px">
    <a style="left:400px">Home</a>
    <a style="left:487px">About Me</a>
    <a style="left:601px">Counseling Services</a>
    <a style="left:799px">Fees</a>
    <a style="left:875px">Blog</a>
    <a style="left:948px">FAQs</a>
    <a style="left:1028px">Contact Me</a>
  </nav>
  <span class="abs social fb" aria-label="Social link"></span>
  <span class="abs social pin" aria-label="Social link"></span>
</header>

<h1 class="abs hero-name">Colette Brannigan</h1>
<p class="abs hero-role">LCSW, Registered Play Therapist</p>

<section class="about">
  <h2 class="abs section-title" style="top:702px">ABOUT Stillbrook</h2>
  <div class="abs about-photo" role="img" aria-label="Portrait photograph of the therapist"></div>
  <p class="abs about-copy">Lorem Ipsum is simply dummy text of the printing and typesetting industry. Lorem Ipsum has been the industry's standard dummy text ever since the 1500s, when an unknown printer took a galley of type and scrambled it to make a type specimen book. It has survived not only five centuries, but also the leap into electronic typesetting, remaining essentially unchanged. It was popularised in the 1960s with the release of Letraset sheets containing Lorem Ipsum passages, and more recently with desktop publishing software like Aldus PageMaker including versions of Lorem Ipsum.</p>
  <div class="abs btn-grey">LEARN MORE</div>
</section>

<section class="abs services"></section>
<h2 class="abs section-title" style="top:1160px">SERVICES We Provide</h2>

<div class="abs svc-icon active" style="left:183px;top:1239px">
  <svg width="60" height="60" viewBox="0 0 60 60" fill="none" stroke="#fff" stroke-width="2.4"><circle cx="30" cy="20" r="10"/><path d="M10 52c0-12 9-18 20-18s20 6 20 18z"/></svg>
</div>
<div class="abs svc-icon" style="left:536px;top:1239px" role="img" aria-label="Play therapy emblem"></div>
<div class="abs svc-icon" style="left:900px;top:1239px" role="img" aria-label="Sand bucket and shovel"></div>

<h3 class="abs svc-title" style="left:76px;top:1383px">Individual Counseling</h3>
<h3 class="abs svc-title" style="left:429px;top:1383px">Play Therapy</h3>
<h3 class="abs svc-title" style="left:793px;top:1383px">Sandplay Therapy</h3>
<p class="abs svc-text" style="left:76px;top:1426px">Lorem Ipsum is simply dummy text of the printing<br>and typesetting industry.</p>
<p class="abs svc-text" style="left:429px;top:1426px">Lorem Ipsum is simply dummy text of the printing<br>and typesetting industry.</p>
<p class="abs svc-text" style="left:793px;top:1426px">Lorem Ipsum is simply dummy text of the printing<br>and typesetting industry.</p>
<p class="abs svc-more" style="left:76px;top:1488px">LEARN MORE</p>
<p class="abs svc-more" style="left:429px;top:1488px">LEARN MORE</p>
<p class="abs svc-more" style="left:793px;top:1488px">LEARN MORE</p>
<p class="abs svc-note">Lorem Ipsum is simply dummy text of the printing and typesetting industry. Lorem Ipsum has been the industry's standard dummy text ever since the 1500s</p>
<div class="abs btn-outline">Book An Appointment</div>

<section class="abs blog"></section>
<h2 class="abs blog-title">BLOG POST</h2>
<p class="abs blog-intro">Check out these recent Hot Topic articles! Visit this page regularly to find links to new articles that will keep you informed and engaged.</p>

<h3 class="abs post-title" style="left:97px;top:1926px">Dear High School Students</h3>
<h3 class="abs post-title" style="left:414px;top:1926px">7 Ways to Cultivate More Thankfulness</h3>
<h3 class="abs post-title" style="left:773px;top:1926px">Selfies Kill More People Than Sharks Do</h3>

<div class="abs post-date" style="left:97px;top:1955px"><svg width="14" height="14" viewBox="0 0 14 14"><rect x="1" y="2" width="12" height="11" fill="#aaa"/><rect x="2.5" y="5.5" width="9" height="6" fill="#e6e6e6"/></svg>Dec 27 2015</div>
<div class="abs post-date" style="left:414px;top:1955px"><svg width="14" height="14" viewBox="0 0 14 14"><rect x="1" y="2" width="12" height="11" fill="#aaa"/><rect x="2.5" y="5.5" width="9" height="6" fill="#e6e6e6"/></svg>Dec 28 2015</div>
<div class="abs post-date" style="left:773px;top:1955px"><svg width="14" height="14" viewBox="0 0 14 14"><rect x="1" y="2" width="12" height="11" fill="#aaa"/><rect x="2.5" y="5.5" width="9" height="6" fill="#e6e6e6"/></svg>Dec 25 2015</div>

<p class="abs post-text" style="left:97px;top:1982px">Don't let your high school years be "the best years of your life...</p>
<p class="abs post-text" style="left:414px;top:1982px">Grow your gratitude with these 7 practical ideas that take 10 minutes or less...</p>
<p class="abs post-text" style="left:773px;top:1982px">Grow your gratitude with these 7 practical ideas that take 10 minutes or less...</p>

<section class="contact">
  <h2 class="abs section-title" style="top:2106px">CONTACT Us</h2>
  <div class="abs field focus" style="left:116px;top:2183px;width:332px;height:49px">Name</div>
  <div class="abs field" style="left:116px;top:2245px;width:332px;height:50px">E - Mail</div>
  <div class="abs field" style="left:116px;top:2306px;width:332px;height:51px">Subject</div>
  <div class="abs field" style="left:459px;top:2183px;width:623px;height:174px">Message</div>
  <div class="abs submit">SUBMIT</div>
</section>

<footer class="abs footer"></footer>
<div class="abs foot-head" style="left:78px;top:2510px">
  <svg width="22" height="28" viewBox="0 0 22 28" fill="var(--sky)"><rect x="9.5" y="0" width="3" height="28"/><rect x="1" y="4" width="20" height="6"/><rect x="1" y="14" width="20" height="6"/></svg>Company Information</div>
<div class="abs foot-head" style="left:435px;top:2510px">
  <svg width="26" height="26" viewBox="0 0 26 26" fill="none" stroke="var(--sky)" stroke-width="2"><path d="M6 2l5 5-3 3c2 4 4 6 8 8l3-3 5 5-4 4C10 23 3 16 2 6z"/></svg>Contact information</div>
<div class="abs foot-head" style="left:793px;top:2510px">
  <svg width="26" height="26" viewBox="0 0 26 26" fill="none" stroke="var(--sky)" stroke-width="2.4"><rect x="2" y="2" width="11" height="11" rx="5" transform="rotate(45 7.5 7.5)"/><rect x="13" y="13" width="11" height="11" rx="5" transform="rotate(45 18.5 18.5)"/></svg>Useful Links</div>

<div class="abs foot-brand"><span class="brand-dot"></span><span class="brand-name">Stillbrook</span></div>
<p class="abs foot-line" style="left:78px;top:2674px;width:310px;font-size:14.5px;line-height:22px">4917 Wexmoor Ln. Idaho Falls, Idaho 83404, US</p>

<p class="abs foot-line" style="left:435px;top:2562px">Phone No. : <span class="foot-link">(208)555-0187</span></p>
<p class="abs foot-line" style="left:435px;top:2603px">E-Mail Address :</p>
<p class="abs foot-line foot-link" style="left:435px;top:2627px">info@stillbrookcounseling.example</p>
<p class="abs foot-line" style="left:435px;top:2666px">Web Address :</p>
<p class="abs foot-line foot-link" style="left:435px;top:2690px">http://www.stillbrookcounseling.example</p>

<p class="abs foot-line" style="left:793px;top:2562px">&gt; <span class="foot-link">Terms &amp; Conditions</span></p>
<p class="abs foot-line" style="left:793px;top:2603px">&gt; Disclaimer</p>
<p class="abs foot-line" style="left:793px;top:2644px">&gt; FAQ's</p>

<div class="abs rule"></div>
<p class="abs copyright">© <span class="foot-link">Stillbrook</span> &nbsp;- 2016 All rights reserved</p>
<span class="abs mini-social" style="left:1066px" aria-label="Social link"></span>
<span class="abs mini-social" style="left:1104px" aria-label="Social link"></span>

</body>
</html>
```